Geschäftspapiere für Jobwebseite
Zielgruppe
Hier finden sie alle Informationen zu unserem Unternehmen:
https://www.blauer-kranich.com
Aufgabenstellung
Gerne von den Farben angelehnt an die Website ein modernes Briefpapier gestalten.

```html
<!DOCTYPE html>
<html lang="de">
<head>
<meta charset="utf-8">
<title>Blauer-Kranich.de – Briefpapier</title>
<link rel="stylesheet" href="https://fonts.googleapis.com/css2?family=Arimo:wght@400;700&family=Tinos&display=swap">
<style>
  :root {
    --ink: #1a1a1a;
    --brand-grey: #4a4f55;
    --photo-dark: #4b4b4b;
    --photo-light: #c9c9c9;
    --green-deep: #9bbd98;
    --green-pale: #eef4ee;
    --white: #ffffff;
  }
  html, body { margin: 0; padding: 0; overflow: hidden; background: var(--white); }
  .sheet {
    position: relative; width: 849px; height: 1200px; overflow: hidden;
    background: var(--white); font-family: "Arimo", Arial, sans-serif; color: var(--ink);
  }
  .sheet__curve { position: absolute; inset: 0; }
  .header-photo {
    position: absolute; left: 525px; top: 0; width: 324px; height: 335px;
    background: linear-gradient(160deg, var(--photo-dark) 0%, #8a8a8a 45%, var(--photo-light) 100%);
  }
  .contact-block {
    position: absolute; left: 537px; top: 220px; margin: 0;
    font-weight: 700; font-size: 14.5px; line-height: 25.6px; color: var(--white);
  }
  .brand-name {
    position: absolute; left: 100px; top: 50px; margin: 0;
    font-weight: 700; font-size: 23px; letter-spacing: 0.5px; color: var(--brand-grey);
  }
  .sender-line {
    position: absolute; left: 99px; top: 161px; margin: 0;
    font-size: 10px; text-decoration: underline;
  }
  .recipient {
    position: absolute; left: 99px; top: 188px; margin: 0;
    font-size: 16.5px; line-height: 20px; font-style: normal;
  }
  .subject {
    position: absolute; left: 98px; top: 343px; margin: 0;
    font-weight: 400; font-size: 24.5px;
  }
  .date {
    position: absolute; right: 103px; top: 387px; margin: 0; font-size: 14.5px;
  }
  .rule {
    position: absolute; left: 100px; top: 443px; width: 643px; height: 0;
    border: 0; border-top: 1.5px solid var(--ink); margin: 0;
  }
  .letter-body {
    position: absolute; left: 100px; top: 465px; margin: 0;
    font-family: "Tinos", "Times New Roman", serif; font-size: 16px; line-height: 19px;
  }
  .letter-body p { margin: 0; }
</style>
</head>
<body>
<main class="sheet">
  <svg class="sheet__curve" width="849" height="1200" viewBox="0 0 849 1200" aria-hidden="true">
    <defs>
      <linearGradient id="curveFill" x1="0.75" y1="0.2" x2="0.35" y2="1">
        <stop offset="0" stop-color="var(--white)"/>
        <stop offset="0.35" stop-color="var(--green-pale)"/>
        <stop offset="1" stop-color="var(--green-deep)"/>
      </linearGradient>
    </defs>
    <path d="M849 345 C 820 720 560 1150 0 1188 L0 1200 L849 1200 Z" fill="url(#curveFill)"/>
  </svg>

  <div class="header-photo" role="img" aria-label="Schwarzweißfoto: Pflegekraft in Kasack mit Stethoskop und Tablet"></div>
  <p class="contact-block">Lindenhof Allee 12<br>76530 Talheim<br>Email: info@blauer-kranich.de<br>Tel:&nbsp; 07221 555 010 9</p>

  <p class="brand-name">BLAUER-KRANICH.de</p>

  <p class="sender-line">Blauer-Kranich.de, Lindenhof Allee 12, 76530 Talheim</p>
  <address class="recipient">Max Mustermann<br>Maxhausener Strasse 55<br>12345 Musterhausen</address>

  <h1 class="subject">Betreff: Ihr neues Briefpapier</h1>
  <p class="date">Datum: 14.03.2018</p>
  <hr class="rule">

  <div class="letter-body">
    <p>Sehr geehrte Damen und Herren,</p>
    <p>…………</p>
    <p>………….</p>
    <p>……………</p>
  </div>
</main>
</body>
</html>
```